Freelance Translator in Need of a Business Card

I am a freelance Japanese to English translator. I work in the video game localization industry and do literary translation in my spare time. I would like to have both the English word 'Translator' and the Japanese '翻訳者' in the job title. The final design should evoke trust, openness, and reliability.

Target Market(s)

Video game localization companies
Japanese comic book artists

Industry/Entity Type

Business

Contact Information for Business Card

Daniel Ostrowik, Translator
dan.ostrowik@quellbox.net
verolingworks.com
twitter: @verol_tx

Colors

Designer to choose colors to be used in the design.

```html
<!DOCTYPE html>
<html lang="en">
<head>
<meta charset="utf-8">
<title>Verol Translates – Business Card</title>
<link rel="stylesheet" href="https://fonts.googleapis.com/css2?family=Playfair+Display:wght@400;700&family=Noto+Serif+JP:wght@400&display=swap">
<style>
  :root {
    --page-bg: #e9e6e1;
    --card-black: #0d0d0d;
    --pattern-tone: #1b1b1b;
    --panel-black: #161616;
    --ink-light: #f4f4f4;
    --ink-soft: #d9d9d9;
    --card-white: #f3f3f3;
    --card-white-edge: #d6d6d6;
    --band-light: #6f8fb0;
    --band-dark: #3e5570;
    --band-text: #f1f3f6;
  }
  * { margin: 0; padding: 0; box-sizing: border-box; }
  html, body {
    width: 1200px; height: 892px; overflow: hidden;
    background: var(--page-bg);
  }
  .canvas {
    width: 1200px; height: 892px;
    display: flex; align-items: center; justify-content: center; gap: 40px;
  }
  .card {
    position: relative;
    width: 540px; height: 309px;
    border-radius: 4px;
    overflow: hidden;
    box-shadow: 0 14px 30px rgba(0,0,0,0.28);
  }
  /* Front */
  .card--front { background: var(--card-black); }
  .card__pattern {
    position: absolute; inset: 0;
    background: radial-gradient(ellipse at 40% 30%, var(--pattern-tone), var(--card-black) 75%);
  }
  .card__panel {
    position: absolute; left: 42px; top: 26px; width: 456px; height: 257px;
    background: var(--panel-black);
    border-radius: 22px;
    display: flex; flex-direction: column; align-items: center; justify-content: center;
    text-align: center;
    color: var(--ink-light);
    font-family: "Playfair Display", Georgia, serif;
  }
  .brand-name { font-size: 34px; font-weight: 700; letter-spacing: 0.5px; line-height: 1.1; }
  .divider {
    width: 100px; height: 1px; margin: 12px 0;
    background: linear-gradient(90deg, transparent, var(--ink-light), transparent);
  }
  .person-name { font-size: 21px; font-weight: 400; line-height: 1.2; }
  .job-title {
    font-size: 13px; color: var(--ink-soft); margin-top: 3px;
  }
  .job-title .jp { font-family: "Noto Serif JP", serif; margin-left: 4px; }
  .contact { font-size: 15px; line-height: 1.45; color: var(--ink-light); }
  /* Back */
  .card--back {
    background: linear-gradient(135deg, #ffffff, var(--card-white) 55%, var(--card-white-edge));
  }
  .band {
    position: absolute; left: 0; right: 0; top: 112px; height: 86px;
    background: linear-gradient(90deg, var(--band-dark), var(--band-light) 35%, var(--band-dark));
    display: flex; align-items: center; justify-content: center;
  }
  .band__name {
    font-family: "Playfair Display", Georgia, serif;
    font-size: 34px; font-weight: 400; letter-spacing: 1.5px;
    color: var(--band-text);
  }
</style>
</head>
<body>
  <main class="canvas">
    <section class="card card--front">
      <div class="card__pattern" role="img" aria-label="Subtle dark geometric diamond pattern background"></div>
      <div class="card__panel">
        <div class="brand-name">Verol Translates</div>
        <div class="divider"></div>
        <div class="person-name">Daniel Ostrowik</div>
        <div class="job-title">Translator<span class="jp">翻訳者</span></div>
        <div class="divider"></div>
        <div class="contact">
          dan.ostrowik@quellbox.net<br>
          www.verolingworks.com<br>
          twitter: @verol_tx
        </div>
      </div>
    </section>
    <section class="card card--back">
      <div class="band">
        <span class="band__name">VEROL TRANSLATES</span>
      </div>
    </section>
  </main>
</body>
</html>
```